Brindo like IOS/Android app for Okinawa Island - LumaTrail

LumaTrail is the name of the app
The closest thing that I can relate this app to is a region specific Brindo app. The app is for the island of Okinawa and is geared towards English speaking travelers. The style of app that I prefer is a look and feel similar to that of the new Nestora app, color should also be similar if not the same as the nestora app.

The app needs to have the following screens

LOGIN SCREEN
1. App login page with a login for chatterly button or create an account option. Personally I would like an image in the background with a real beachy feel, but don't do this if it messes with your design.

2. Depending on the choice of login there will need to be a second login screen to create the account. Nestora does this nicely.

PRIMARY HOME
primary page similar to the primary layout when you get into the nestora app.
This page is kind of like the home page of the app and should include the following items:
search field
upcoming events
popular things to do
featured restaurants
Featured Places to stay
area guides
Moving here
(this will allow the person to select, housing agencies, auto dealers, schools etc) These are essentially just quick searches.
Each selection should be listed so that the user can swipe to the left or right in order to view more listings under the categories listed above. It will not be the full list but rather a sample.

SIDEBAR POPOUT MENU
Popout sidebar that contains the following selections
Places to Eat
Things to do
Attractions
Beaches
Shop
Farmers Markets
Places to Stay
Schools & DayCare
Housing
Auto
Events
Account settings
Add a business

LIST VIEW
4. List view page for whatever category the user selected. This will show all the listings for the specific category: The top should also have the featured listings for that category

INDIVIDUAL LISTING
5. Listing page
This will include photos, description, hours, map(this can be a button to view the map or the map), Reviews with a leave a review option

AREA GUIDES
6. Area Guides. This is where the user will be able to select a specific area and learn about it. It should include an area where there can be a description, photos with a hero photo image, a map, popular local attractions or things to do, best restaurants in the area, places to stay etc.

PROFILE PAGE
7. Profile page for the user where they can make any updates they need to

Every page but the listing page should include the search bar. When the user clicks in it they should be able to see a drop down of quick select searches or run a regular search.

Logo
I have attached a logo that was made that needs a redesign. The map marker contains the logo for Okinawa within it so it does need to be similar.

If you have any questions or need clarification please send me a message. I will respond promptly.
Thank you,

```html
<!DOCTYPE html>
<html lang="en">
<head>
<meta charset="utf-8">
<title>LumaTrail: First and login screens flow</title>
<link href="https://fonts.googleapis.com/css2?family=Mulish:wght@300;400;500;600;700;800&family=Roboto:wght@400&display=swap" rel="stylesheet">
<style>
  :root {
    --board: #fefbea;
    --ink: #3d3d3d;
    --berry: #b93a5e;
    --plum: #6b2d7a;
    --paper: #f3f3f6;
    --sky: #aad7ea;
    --lagoon: #5ec9d2;
    --keyboard: #d1d5db;
    --key: #ffffff;
    --key-dark: #abb2bc;
  }
  * { box-sizing: border-box; margin: 0; padding: 0; }
  html, body { width: 1200px; height: 960px; overflow: hidden; }
  body {
    background: var(--board);
    font-family: "Mulish", sans-serif;
    position: relative;
  }
  .board-title {
    position: absolute; top: 142px; left: 0; width: 1200px;
    text-align: center; font-size: 37px; font-weight: 300;
    color: var(--ink); letter-spacing: 0.2px;
  }
  .board-title strong { font-weight: 500; }

  .screen {
    position: absolute; top: 265px; width: 300px; height: 533px;
    overflow: hidden; box-shadow: 0 1px 3px rgba(0,0,0,0.12);
  }
  .screen--welcome { left: 258px; background: var(--paper); }
  .screen--login { left: 642px; background: var(--sky); }

  .status-bar {
    position: absolute; top: 0; left: 0; right: 0; height: 16px;
    display: flex; align-items: center; justify-content: space-between;
    padding: 0 5px; font-size: 8px; color: #111;
    font-family: "Roboto", sans-serif;
  }
  .status-bar__time { position: absolute; left: 0; right: 0; text-align: center; }
  .status-bar__left, .status-bar__right { display: flex; align-items: center; gap: 3px; position: relative; z-index: 1; }
  .battery { width: 17px; height: 7px; border: 1px solid #111; border-radius: 1px; position: relative; }
  .battery::before { content: ""; position: absolute; left: 1px; top: 1px; bottom: 1px; width: 11px; background: #111; }

  .top-link {
    position: absolute; top: 30px; font-size: 13px; color: var(--plum);
  }
  .screen--welcome .top-link { right: 21px; }
  .screen--login .top-link { right: 17px; }

  .brand {
    position: absolute; top: 138px; left: 82px;
    display: flex; align-items: center; gap: 10px;
  }
  .brand__dot { width: 26px; height: 26px; border-radius: 50%; background: var(--berry); }
  .brand__name { font-size: 21px; font-weight: 700; color: var(--plum); letter-spacing: 0.3px; }

  .beach-photo {
    position: absolute; left: 0; right: 0; top: 300px; bottom: 0;
    background: linear-gradient(180deg, var(--paper) 0%, var(--lagoon) 100%);
  }

  .btn {
    position: absolute; left: 29px; width: 244px; height: 43px; border-radius: 22px;
    display: flex; align-items: center; justify-content: center; gap: 10px;
    font-family: "Mulish", sans-serif; font-size: 14px;
  }
  .btn--social { top: 217px; background: var(--berry); color: #fff; }
  .btn--social .btn__dot { width: 18px; height: 18px; border-radius: 50%; background: #fff; }
  .btn--outline { top: 274px; height: 42px; border: 1px solid var(--berry); color: var(--berry); background: transparent; }

  .back-arrow { position: absolute; top: 31px; left: 18px; }
  .login-title {
    position: absolute; top: 92px; left: 26px;
    font-size: 24px; font-weight: 700; color: var(--plum);
  }
  .field { position: absolute; left: 26px; width: 250px; }
  .field__label { font-size: 11px; font-weight: 600; color: var(--plum); letter-spacing: 0.2px; }
  .field__line { height: 1px; background: var(--plum); opacity: 0.8; margin-top: 38px; }
  .field--email { top: 158px; }
  .field--password { top: 231px; }
  .btn--login {
    position: absolute; top: 300px; left: 94px; width: 112px; height: 43px; border-radius: 22px;
    background: var(--berry); color: #fff; font-size: 14px;
    display: flex; align-items: center; justify-content: center;
  }

  .keyboard {
    position: absolute; left: 0; right: 0; top: 361px; bottom: 0;
    background: var(--keyboard); padding: 7px 3px 0;
    font-family: "Roboto", sans-serif;
  }
  .key-row { display: flex; justify-content: center; gap: 5px; margin-bottom: 9px; }
  .key {
    width: 25px; height: 34px; background: var(--key); border-radius: 4px;
    box-shadow: 0 1px 0 #888e96; display: flex; align-items: center; justify-content: center;
    font-size: 17px; color: #111;
  }
  .key--dark { background: var(--key-dark); }
  .key--shift, .key--delete { width: 34px; }
  .key-row--shift { justify-content: space-between; }
  .key-row--shift .letters { display: flex; gap: 5px; }
  .key--num { width: 34px; font-size: 12px; }
  .key--emoji { width: 34px; }
  .key--mic { width: 25px; }
  .key--space { width: 115px; font-size: 12px; }
  .key--return { width: 69px; font-size: 12px; }
</style>
</head>
<body>
  <h1 class="board-title"><strong>LumaTrail:</strong> First and login screens flow</h1>

  <section class="screen screen--welcome">
    <div class="beach-photo" role="img" aria-label="Photo of a turquoise sea and white sand beach under a blue sky"></div>
    <div class="status-bar">
      <span class="status-bar__left">●●●○○ CL
        <svg width="9" height="7" viewBox="0 0 9 7"><path d="M0.5 2.5a6 6 0 0 1 8 0M2 4a3.7 3.7 0 0 1 5 0M3.5 5.5a1.5 1.5 0 0 1 2 0" stroke="#111" fill="none" stroke-width="1"/></svg>
      </span>
      <span class="status-bar__time">1:20 PM</span>
      <span class="status-bar__right">✱ 77% <span class="battery"></span></span>
    </div>
    <a class="top-link">Log in</a>
    <div class="brand">
      <span class="brand__dot"></span>
      <span class="brand__name">lumatrail</span>
    </div>
    <div class="btn btn--social"><span class="btn__dot"></span>Continue with Chatterly</div>
    <div class="btn btn--outline">Create Account</div>
  </section>

  <section class="screen screen--login">
    <div class="status-bar">
      <span class="status-bar__left">●●●○○ CL
        <svg width="9" height="7" viewBox="0 0 9 7"><path d="M0.5 2.5a6 6 0 0 1 8 0M2 4a3.7 3.7 0 0 1 5 0M3.5 5.5a1.5 1.5 0 0 1 2 0" stroke="#111" fill="none" stroke-width="1"/></svg>
      </span>
      <span class="status-bar__time">1:20 PM</span>
      <span class="status-bar__right">✱ 77% <span class="battery"></span></span>
    </div>
    <svg class="back-arrow" width="9" height="14" viewBox="0 0 9 14" aria-label="Back"><path d="M7.5 1 1.5 7l6 6" stroke="#6b2d7a" stroke-width="1.8" fill="none" stroke-linecap="round" stroke-linejoin="round"/></svg>
    <a class="top-link">Forgot password?</a>
    <h2 class="login-title">Log in</h2>
    <div class="field field--email">
      <div class="field__label">EMAIL ADDRESS</div>
      <div class="field__line"></div>
    </div>
    <div class="field field--password">
      <div class="field__label">PASSWORD</div>
      <div class="field__line"></div>
    </div>
    <div class="btn--login">Login</div>

    <div class="keyboard">
      <div class="key-row">
        <span class="key">Q</span><span class="key">W</span><span class="key">E</span><span class="key">R</span><span class="key">T</span><span class="key">Y</span><span class="key">U</span><span class="key">I</span><span class="key">O</span><span class="key">P</span>
      </div>
      <div class="key-row">
        <span class="key">A</span><span class="key">S</span><span class="key">D</span><span class="key">F</span><span class="key">G</span><span class="key">H</span><span class="key">J</span><span class="key">K</span><span class="key">L</span>
      </div>
      <div class="key-row key-row--shift">
        <span class="key key--shift"><svg width="14" height="13" viewBox="0 0 14 13"><path d="M7 1 1 7h3.5v5h5V7H13z" fill="#111"/></svg></span>
        <span class="letters"><span class="key">Z</span><span class="key">X</span><span class="key">C</span><span class="key">V</span><span class="key">B</span><span class="key">N</span><span class="key">M</span></span>
        <span class="key key--dark key--delete"><svg width="18" height="12" viewBox="0 0 18 12"><path d="M5 1h12v10H5L1 6z" fill="none" stroke="#111" stroke-width="1.2" stroke-linejoin="round"/><path d="m8.5 3.5 5 5m0-5-5 5" stroke="#111" stroke-width="1.2"/></svg></span>
      </div>
      <div class="key-row">
        <span class="key key--dark key--num">123</span>
        <span class="key key--dark key--emoji"><svg width="17" height="17" viewBox="0 0 17 17"><circle cx="8.5" cy="8.5" r="7.5" fill="none" stroke="#111" stroke-width="1.2"/><circle cx="6" cy="7" r="1" fill="#111"/><circle cx="11" cy="7" r="1" fill="#111"/><path d="M4.5 10h8a4 4 0 0 1-8 0z" fill="#111"/></svg></span>
        <span class="key key--mic"><svg width="10" height="17" viewBox="0 0 10 17"><rect x="3" y="1" width="4" height="9" rx="2" fill="none" stroke="#111" stroke-width="1.2"/><path d="M1 8a4 4 0 0 0 8 0M5 12v4M3 16h4" fill="none" stroke="#111" stroke-width="1.2"/></svg></span>
        <span class="key key--space">space</span>
        <span class="key key--dark key--return">return</span>
      </div>
    </div>
  </section>
</body>
</html>
```